Velvetmoth chocolates label & packaging design

We make high end chocolates .Enrobed medjoul dates ,truffles and filled chocolates . We have to upgrade our packaging to reflect the quality of the products
1 . Chocolate box label or sleeve for
1a truffle box
2a enrobed date box
3a Chocolate box
4a Mixed chocolate truffle and date box .
I also have a project in mind to make hot chocolate kits which would be our hot chocolate powder chocolate & home made marshmallows.
The images attached should give an idea of the products The label designs included are an example of the colour palette we like .
We would like to include the velvetmoth logo as part of the design .
Our chocolates are made without adding. Dairy or refined sugars and using the best ingredients available .

Target Market(s)

Food lovers, those who prioritise quality above quantity .

Industry/Entity Type

Chocolatier

Font styles to use
Script

Colors
0054AA
0677BA
7BADD7
CADEEF
E8F1F8
F0912C
F2A743
F7CA91
FBE8D2
FDF5EE
E54698
E96AAD
F1A4CE
F9D9EA
FCEFF6

Requirements
Must have
• An element of luxury
Nice to have
• Something to reflect the integrity of the ingredients and the love that goes into making the chocolates.
Should not have
• Too much packaging

```html
<!DOCTYPE html>
<html lang="en">
<head>
<meta charset="utf-8">
<title>Velvetmoth box labels</title>
<link rel="stylesheet" href="https://fonts.googleapis.com/css2?family=Poiret+One&family=Dancing+Script:wght@400&display=swap">
<style>
  :root {
    --page: #ffffff;
    --kraft: #d8c8b1;
    --kraft-light: #ddcdb7;
    --ink: #2b2d45;
    --rose: #b07c8b;
    --slate: #4a5669;
    --mist: #b4d2d4;
    --logo-card: #fdf9f3;
  }
  * { box-sizing: border-box; margin: 0; padding: 0; }
  html, body {
    width: 1200px; height: 1038px; overflow: hidden; background: var(--page);
  }
  .canvas { position: relative; width: 1200px; height: 1038px; }

  .label {
    position: absolute; top: 246px; width: 302px; height: 521px;
    border-radius: 6px; overflow: hidden; background: var(--band);
  }
  .label--chocolates { left: 109px; --band: var(--rose); }
  .label--truffles   { left: 447px; --band: var(--slate); }
  .label--dates      { left: 794px; --band: var(--mist); }

  .kraft-panel {
    position: absolute; left: 39px; right: 38px; top: 0; bottom: 16px;
    background: radial-gradient(circle at 40% 30%, var(--kraft-light), var(--kraft) 70%);
  }
  .title-band, .foot-band {
    position: absolute; left: 0; right: 0; background: var(--kraft);
  }
  .title-band { top: 47px; height: 48px; }
  .foot-band  { top: 467px; height: 39px; }
  .foot-band .dot {
    position: absolute; right: 36px; top: 21px; width: 3px; height: 3px;
    border-radius: 50%; background: #8a7760;
  }
  .zigzag { position: absolute; left: 0; top: 505px; width: 302px; height: 8px; }

  .title {
    position: absolute; left: 0; right: 0; top: 50px; text-align: center;
    font-family: "Poiret One", sans-serif; color: var(--ink);
    text-transform: uppercase; white-space: nowrap; line-height: 1;
  }
  .title .cap { font-size: 1.32em; }
  .label--chocolates .title { font-size: 34px; top: 54px; letter-spacing: 1px; }
  .label--truffles .title   { font-size: 46px; top: 44px; letter-spacing: 1px; }
  .label--dates .title      { font-size: 29px; top: 57px; letter-spacing: 0; }

  .brand-card {
    position: absolute; left: 102px; top: 155px; width: 98px; height: 98px;
    background: var(--logo-card); border: 2px solid #3a3633;
    outline: 1px solid #3a3633; outline-offset: 3px;
    display: flex; align-items: center; justify-content: center;
  }
  .brand-name {
    font-family: "Dancing Script", cursive; font-size: 19px; color: var(--ink);
  }

  .claims {
    position: absolute; left: 0; right: 0; top: 318px; list-style: none;
    text-align: center; font-family: "Dancing Script", cursive;
    font-size: 16px; line-height: 29px; color: var(--ink);
  }
  .claims .cont { padding-left: 6px; }
  .tagline {
    position: absolute; left: 0; right: 0; top: 474px; text-align: center;
    font-family: "Dancing Script", cursive; font-size: 18px; color: var(--ink);
  }
</style>
</head>
<body>
<main class="canvas">

  <section class="label label--chocolates">
    <div class="kraft-panel"></div>
    <div class="title-band"></div>
    <div class="foot-band"><span class="dot"></span></div>
    <svg class="zigzag" viewBox="0 0 302 8" preserveAspectRatio="none"><polygon fill="#d8c8b1" points="0,0 302,0 302,2 298,8 294,2 290,8 286,2 282,8 278,2 274,8 270,2 266,8 262,2 258,8 254,2 250,8 246,2 242,8 238,2 234,8 230,2 226,8 222,2 218,8 214,2 210,8 206,2 202,8 198,2 194,8 190,2 186,8 182,2 178,8 174,2 170,8 166,2 162,8 158,2 154,8 150,2 146,8 142,2 138,8 134,2 130,8 126,2 122,8 118,2 114,8 110,2 106,8 102,2 98,8 94,2 90,8 86,2 82,8 78,2 74,8 70,2 66,8 62,2 58,8 54,2 50,8 46,2 42,8 38,2 34,8 30,2 26,8 22,2 18,8 14,2 10,8 6,2 2,8 0,2"/></svg>
    <h2 class="title"><span class="cap">C</span>hocolates</h2>
    <div class="brand-card"><span class="brand-name">Velvetmoth</span></div>
    <ul class="claims">
      <li>· We use fair trade dates</li>
      <li>· Single origin ethically</li>
      <li class="cont">sourced Chocolate</li>
      <li>· We dont add dairy grains</li>
      <li class="cont">or refined sugars</li>
    </ul>
    <p class="tagline">Made with love in west cork</p>
  </section>

  <section class="label label--truffles">
    <div class="kraft-panel"></div>
    <div class="title-band"></div>
    <div class="foot-band"><span class="dot"></span></div>
    <svg class="zigzag" viewBox="0 0 302 8" preserveAspectRatio="none"><polygon fill="#d8c8b1" points="0,0 302,0 302,2 298,8 294,2 290,8 286,2 282,8 278,2 274,8 270,2 266,8 262,2 258,8 254,2 250,8 246,2 242,8 238,2 234,8 230,2 226,8 222,2 218,8 214,2 210,8 206,2 202,8 198,2 194,8 190,2 186,8 182,2 178,8 174,2 170,8 166,2 162,8 158,2 154,8 150,2 146,8 142,2 138,8 134,2 130,8 126,2 122,8 118,2 114,8 110,2 106,8 102,2 98,8 94,2 90,8 86,2 82,8 78,2 74,8 70,2 66,8 62,2 58,8 54,2 50,8 46,2 42,8 38,2 34,8 30,2 26,8 22,2 18,8 14,2 10,8 6,2 2,8 0,2"/></svg>
    <h2 class="title">Truffles</h2>
    <div class="brand-card"><span class="brand-name">Velvetmoth</span></div>
    <ul class="claims">
      <li>· We use fair trade dates</li>
      <li>· Single origin ethically</li>
      <li class="cont">sourced Chocolate</li>
      <li>· We dont add dairy grains</li>
      <li class="cont">or refined sugars</li>
    </ul>
    <p class="tagline">Made with love in west cork</p>
  </section>

  <section class="label label--dates">
    <div class="kraft-panel"></div>
    <div class="title-band"></div>
    <div class="foot-band"><span class="dot"></span></div>
    <svg class="zigzag" viewBox="0 0 302 8" preserveAspectRatio="none"><polygon fill="#d8c8b1" points="0,0 302,0 302,2 298,8 294,2 290,8 286,2 282,8 278,2 274,8 270,2 266,8 262,2 258,8 254,2 250,8 246,2 242,8 238,2 234,8 230,2 226,8 222,2 218,8 214,2 210,8 206,2 202,8 198,2 194,8 190,2 186,8 182,2 178,8 174,2 170,8 166,2 162,8 158,2 154,8 150,2 146,8 142,2 138,8 134,2 130,8 126,2 122,8 118,2 114,8 110,2 106,8 102,2 98,8 94,2 90,8 86,2 82,8 78,2 74,8 70,2 66,8 62,2 58,8 54,2 50,8 46,2 42,8 38,2 34,8 30,2 26,8 22,2 18,8 14,2 10,8 6,2 2,8 0,2"/></svg>
    <h2 class="title"><span class="cap">E</span>nrobed dates</h2>
    <div class="brand-card"><span class="brand-name">Velvetmoth</span></div>
    <ul class="claims">
      <li>· We use fair trade dates</li>
      <li>· Single origin ethically</li>
      <li class="cont">sourced Chocolate</li>
      <li>· We dont add dairy grains</li>
      <li class="cont">or refined sugars</li>
    </ul>
    <p class="tagline">Made with love in west cork</p>
  </section>

</main>
</body>
</html>
```